依頼詳細
バイクで周辺のニュータウンに配布を考えています。
量販店よりもかなり安いので、安いとわかるようなチラシに仕上げたいです。
また、片面にウォーターサーバーのサブスクの内容を入れてます。
デザインは近いものでイラストを考えています。
記載項目
社名・電話番号・料金プラン
エアコンの取付・取外しをお得にできます。
エアコン基本設置4m 11,000円~
エアコン基本外し 4,000円(2台台以上)
(外し単品は6,000円)
価格は税込み
サイズ
A5
ページ数
片面
希望イメージ
シンプル 複雑
単色 カラフル
暗い 明るい
日常 高級
遊び心 厳粛
未来的 伝統的
女性的 男性的
希望する色
黄・オレンジ系
納品ファイル
• イラストレーター形式 (.ai)
補足説明
■ 選んだ理由

こちらで想定していたのと全然違う構成に感銘を受けました。
かなり手直しが必要ですが、こちらの路線でチラシを作成しようと思います。

■ 提案者全員のお礼・コメント

今回はたくさんのご応募をいただき大変感謝しております。
たくさんのパターンがあり感動しています。
また、同じような応募をしますのでその際はよろしくお願いいたします

```html
<!DOCTYPE html>
<html lang="ja">
<head>
<meta charset="utf-8">
<title>エアコン取付・取外し チラシ</title>
<link rel="stylesheet" href="https://fonts.googleapis.com/css2?family=Noto+Sans+JP:wght@500;700;900&display=swap">
<style>
  :root {
    --sun-yellow: #ffd21f;
    --sun-light: #ffe866;
    --navy: #1f2f5c;
    --orange: #f08a12;
    --orange-deep: #e8590c;
    --green: #3fae49;
    --amber: #f6a71b;
    --red-orange: #ee5a1e;
    --white: #ffffff;
    --ink: #222833;
    --ac-grey: #e6e9ee;
    --worker-blue: #6f8fb8;
  }
  * { margin: 0; padding: 0; box-sizing: border-box; }
  html, body { width: 844px; height: 1200px; overflow: hidden; background: var(--white); }
  body { font-family: "Noto Sans JP", sans-serif; color: var(--ink); }

  .flyer { position: relative; width: 844px; height: 1200px; overflow: hidden;
    background: radial-gradient(circle at 50% 30%, var(--sun-light) 0%, var(--sun-yellow) 60%, #ffc414 100%); }

  .aircon { position: absolute; left: 120px; top: 0; width: 604px; height: 230px;
    background: linear-gradient(180deg, #f7f8fa 0%, var(--ac-grey) 100%);
    border-radius: 0 0 40px 40px; box-shadow: 0 8px 18px rgba(0,0,0,.15); }

  .worker { position: absolute; top: 280px; width: 170px; height: 220px;
    background: linear-gradient(180deg, #9fb4d1 0%, var(--worker-blue) 100%); border-radius: 80px 80px 20px 20px; }
  .worker--left { left: 30px; }
  .worker--right { right: 30px; }

  .headline { position: absolute; top: 268px; left: 0; width: 100%; text-align: center; }
  .headline__lead { display: inline-block; background: var(--navy); color: var(--white);
    font-weight: 900; font-size: 38px; padding: 4px 26px; border-radius: 8px; letter-spacing: 1px; }
  .headline__main { margin-top: 6px; font-weight: 900; font-size: 80px; line-height: 1.1;
    color: var(--navy); -webkit-text-stroke: 0; text-shadow: 4px 4px 0 var(--white), -3px -3px 0 var(--white), 3px -3px 0 var(--white), -3px 3px 0 var(--white); }
  .headline__main em { font-style: normal; color: var(--orange-deep); }

  .tagline { position: absolute; top: 430px; left: 0; width: 100%; text-align: center;
    font-weight: 900; font-size: 26px; color: var(--navy); }
  .tagline em { font-style: normal; color: var(--orange-deep); }
  .tagline__note { display: block; margin-top: 4px; font-size: 15px; font-weight: 700; color: var(--navy); }

  .plans { position: absolute; top: 515px; left: 0; width: 100%; }
  .plan { position: relative; height: 150px; margin-bottom: 14px; display: flex; align-items: center;
    padding-left: 22px; }
  .plan--install { background: linear-gradient(90deg, var(--orange), var(--amber)); }
  .plan--remove { background: var(--green); }
  .plan--multi { background: linear-gradient(90deg, var(--red-orange), var(--orange)); }

  .plan__badge { position: relative; width: 96px; height: 96px; border-radius: 50%; background: var(--white);
    display: flex; align-items: center; justify-content: center; font-weight: 900; font-size: 58px;
    color: var(--orange-deep); border: 6px solid var(--orange-deep); flex-shrink: 0; }
  .plan__badge-tag { position: absolute; top: -8px; left: -8px; width: 34px; height: 34px; border-radius: 50%;
    background: var(--navy); color: var(--white); font-size: 18px; display: flex; align-items: center; justify-content: center; }
  .plan__label { margin-left: 14px; width: 190px; background: var(--white); border-radius: 10px;
    padding: 10px 14px; font-weight: 900; font-size: 28px; line-height: 1.2; color: var(--ink); }
  .plan__label small { display: block; font-size: 15px; font-weight: 700; }
  .plan__price { margin-left: 26px; color: var(--white); font-weight: 900; font-size: 84px; letter-spacing: 1px;
    text-shadow: 3px 3px 0 rgba(0,0,0,.18); display: flex; align-items: flex-end; }
  .plan__price .yen { font-size: 50px; margin-bottom: 10px; }
  .plan__price .tax { font-size: 20px; margin-bottom: 50px; margin-left: 4px; }

  .footer { position: absolute; left: 0; bottom: 0; width: 100%; height: 180px; background: var(--white);
    padding: 18px 30px; }
  .footer__row { display: flex; align-items: center; justify-content: space-between; }
  .footer__company { font-weight: 900; font-size: 28px; }
  .footer__contact { background: var(--green); color: var(--white); font-weight: 700; font-size: 18px;
    padding: 5px 20px; border-radius: 20px; }
  .footer__note { font-size: 16px; font-weight: 700; }
  .footer__phone { margin-top: 16px; display: flex; align-items: center; gap: 22px; }
  .footer__phone-mark { width: 92px; height: 92px; border-radius: 50%; background: var(--orange-deep); }
  .footer__phone-number { font-weight: 900; font-size: 86px; letter-spacing: 2px; line-height: 1; }
</style>
</head>
<body>
<div class="flyer">
  <div class="aircon" role="img" aria-label="壁掛けエアコンのイラスト"></div>
  <div class="worker worker--left" role="img" aria-label="作業服の作業員のイラスト"></div>
  <div class="worker worker--right" role="img" aria-label="工具を持つ作業員のイラスト"></div>

  <div class="headline">
    <div class="headline__lead">エアコンの取付・取外しを</div>
    <div class="headline__main"><em>お得</em>にできます</div>
  </div>

  <p class="tagline">引越しや移設、買い替え時は<em>ミライ</em>にお任せ!
    <span class="tagline__note">量販店よりもかなり安くなっております!</span></p>

  <section class="plans">
    <div class="plan plan--install">
      <div class="plan__badge">得</div>
      <div class="plan__label">エアコン<br>基本設置<small>(4メートル)</small></div>
      <div class="plan__price">11,000<span class="yen">円~</span><span class="tax">(税込)</span></div>
    </div>
    <div class="plan plan--remove">
      <div class="plan__badge">得</div>
      <div class="plan__label">エアコン<br>基本外し<small>(1台)</small></div>
      <div class="plan__price">6,000<span class="yen">円</span><span class="tax">(税込)</span></div>
    </div>
    <div class="plan plan--multi">
      <div class="plan__badge"><span class="plan__badge-tag">超</span>得</div>
      <div class="plan__label">エアコン<br>基本外し<small>(2台以上)</small></div>
      <div class="plan__price">4,000<span class="yen">円</span><span class="tax">(税込)</span></div>
    </div>
  </section>

  <footer class="footer">
    <div class="footer__row">
      <div class="footer__company">株式会社ミライ</div>
      <div class="footer__contact">お申し込み・お問い合わせはこちら</div>
      <div class="footer__note">お気軽にご相談ください!</div>
    </div>
    <div class="footer__phone">
      <span class="footer__phone-mark"></span>
      <span class="footer__phone-number">0120-000-123</span>
    </div>
  </footer>
</div>
</body>
</html>
```